Business Card for Multi-Brand Sportswear Company

We are looking for a business card which represents our company and the multiple brands within it.

The company: Kelt Athletic (LTD)
The brands: Kelt, PawaLuni, VerdantFlex, Grit and Gale

Employees using these cards would be representing Kelt Athletic, rather than any of the individual brands. You will see a current design within the uploaded files, to give some inspiration. The actual text of the brands is not necessary, but the logos should be on there is some format.

Our creative minds on this are stretched, so we are looking for someone to make this their own, and show us what a good business card should look like.

We may like to get these printed with spot gloss, so keep that in mind with your designs.

www.keltathletic.co.uk

Industry/Entity Type

Business

Contact Information for Business Card

Tom Hollingsworth-Pryce
Operations Manager
(+44) 1632 960 418
Tom@keltathletic.co.uk
www.keltathletic.co.uk

Font styles to use
Sans Serif
Other font styles liked:
• Eurostile

Colors
ffffff

Requirements
Nice to have
• Dark (black) background

```html
<!DOCTYPE html>
<html lang="en">
<head>
<meta charset="utf-8">
<title>Kelt Athletic – Business Card</title>
<link href="https://fonts.googleapis.com/css2?family=Michroma&family=Exo+2:wght@300;400;700&display=swap" rel="stylesheet">
<style>
  :root {
    --backdrop: #e4e4e4;
    --card: #0d0d0d;
    --ink: #ffffff;
    --ink-soft: #cfcfcf;
    --accent: #e3222b;
    --display: "Michroma", sans-serif;
    --text: "Exo 2", sans-serif;
  }
  * { margin: 0; padding: 0; box-sizing: border-box; }
  html, body { width: 1200px; height: 750px; overflow: hidden; }
  body {
    background: var(--backdrop);
    position: relative;
    font-family: var(--text);
    color: var(--ink);
  }
  .card {
    position: absolute;
    top: 220px;
    width: 540px;
    height: 309px;
    background: var(--card);
    overflow: hidden;
  }
  .card--contact { left: 40px; }
  .card--brand { left: 620px; }
  .card__bands { position: absolute; inset: 0; }
  .band { fill: var(--accent); }

  /* wordmark */
  .wordmark {
    position: absolute;
    text-align: right;
    font-family: var(--display);
    color: var(--ink);
  }
  .wordmark__name { display: block; text-transform: uppercase; letter-spacing: 0.04em; }
  .wordmark__tagline {
    display: block;
    font-family: var(--text);
    font-weight: 300;
    text-transform: uppercase;
    letter-spacing: 0.12em;
    color: var(--ink-soft);
  }
  .card--contact .wordmark { top: 22px; right: 26px; }
  .card--contact .wordmark__name { font-size: 17px; }
  .card--contact .wordmark__tagline { font-size: 8px; margin-top: 3px; }

  .card--brand .wordmark { top: 122px; left: 0; right: 0; text-align: center; }
  .card--brand .wordmark__name { font-size: 32px; }
  .card--brand .wordmark__tagline { font-size: 12px; margin-top: 8px; letter-spacing: 0.3em; }

  /* person */
  .person { position: absolute; left: 36px; top: 84px; }
  .person__name {
    font-weight: 700;
    font-size: 13px;
    letter-spacing: 0.06em;
    text-transform: uppercase;
  }
  .person__role {
    margin-top: 6px;
    font-weight: 300;
    font-size: 11px;
    letter-spacing: 0.14em;
    text-transform: uppercase;
    color: var(--ink-soft);
  }

  /* contact list */
  .contact-list {
    position: absolute;
    top: 76px;
    right: 26px;
    list-style: none;
    font-size: 10.5px;
    letter-spacing: 0.04em;
  }
  .contact-list__item {
    display: flex;
    align-items: center;
    gap: 12px;
    height: 22px;
  }
  .contact-list__icon { width: 12px; height: 12px; fill: none; stroke: var(--ink); stroke-width: 1.4; }

  /* brand family row */
  .brand-row {
    position: absolute;
    left: 36px;
    bottom: 26px;
    display: flex;
    gap: 18px;
    align-items: center;
    list-style: none;
    font-size: 10px;
    font-weight: 400;
    letter-spacing: 0.08em;
    text-transform: uppercase;
    color: var(--ink);
  }

  .card__url {
    position: absolute;
    right: 28px;
    bottom: 66px;
    font-size: 14px;
    letter-spacing: 0.06em;
    color: var(--ink);
  }
</style>
</head>
<body>

  <!-- Contact side -->
  <section class="card card--contact">
    <svg class="card__bands" viewBox="0 0 540 309" aria-hidden="true">
      <polygon class="band" points="0,60 330,60 320,70 0,70"/>
      <polygon class="band" points="300,176 540,176 540,186 292,186"/>
    </svg>

    <div class="wordmark">
      <span class="wordmark__name">Kelt Athletic</span>
      <span class="wordmark__tagline">Performance Wear</span>
    </div>

    <div class="person">
      <p class="person__name">Tom Hollingsworth-Pryce</p>
      <p class="person__role">Operations Manager</p>
    </div>

    <ul class="contact-list">
      <li class="contact-list__item">
        <svg class="contact-list__icon" viewBox="0 0 12 12" aria-hidden="true"><path d="M2 1 L4.5 1 L5.5 3.5 L4 4.5 Q5 7 7.5 8 L8.5 6.5 L11 7.5 L11 10 Q6 11 2 6 Q1 3.5 2 1 Z" fill="#fff" stroke="none"/></svg>
        <span>(+44) 1632 960 418</span>
      </li>
      <li class="contact-list__item">
        <svg class="contact-list__icon" viewBox="0 0 12 12" aria-hidden="true"><rect x="0.7" y="2" width="10.6" height="8"/><path d="M0.7 2 L6 6.5 L11.3 2"/></svg>
        <span>Tom@keltathletic.co.uk</span>
      </li>
      <li class="contact-list__item">
        <svg class="contact-list__icon" viewBox="0 0 12 12" aria-hidden="true"><circle cx="6" cy="6" r="5.2"/><ellipse cx="6" cy="6" rx="2.2" ry="5.2"/><path d="M0.8 6 H11.2"/></svg>
        <span>www.keltathletic.co.uk</span>
      </li>
    </ul>

    <ul class="brand-row">
      <li>Kelt</li>
      <li>PawaLuni</li>
      <li>VerdantFlex</li>
      <li>Grit and Gale</li>
    </ul>
  </section>

  <!-- Brand side -->
  <section class="card card--brand">
    <svg class="card__bands" viewBox="0 0 540 309" aria-hidden="true">
      <polygon class="band" points="180,30 540,30 540,40 172,40"/>
      <polygon class="band" points="0,262 360,262 350,272 0,272"/>
    </svg>

    <div class="wordmark">
      <span class="wordmark__name">Kelt Athletic</span>
      <span class="wordmark__tagline">Performance Wear</span>
    </div>

    <p class="card__url">www.keltathletic.co.uk</p>
  </section>

</body>
</html>
```